Fitness Equipment Repair Business Needs a Catchy New Business Card

We have an existing business card, however, it is quite plain and boring. We are expanding primarily in the commercial area (gyms, studios, apartment complexes etc). The business card will serve as eye candy to those managers/owners that can't be met for a face to face.
Originally I was planning for a brochure as well, but all of our information is better summarized on our website. (brasswheelservicing.ca).
I would like the card to match the colour scheme of the website and utilize the logo. It should have a professional clean feel to it, however, a little colouring outside the lines wouldn't hurt.
The example card is for my service technician (Corwin Haldane). If possible I would like to be able to edit the text to use for more than one person.

Industry/Entity Type

Appliance Repair

Contact Information for Business Card

Clean, crisp and professional but needs to be eye catching. Preferably using the black, white and red colour scheme matching the website. Double sided would be nice, but is not necessary.

Colors
ec1f27
ffffff
000000

Requirements
Must have
• Must be able to edit name, phone number and title to use for multiple people. Must show the company website (brasswheelservicing.ca).

```html
<!DOCTYPE html>
<html lang="en">
<head>
<meta charset="utf-8">
<title>Brass Wheel Servicing – Business Card</title>
<link rel="stylesheet" href="https://fonts.googleapis.com/css2?family=Raleway:wght@300;400&display=swap">
<style>
  :root {
    --brand-red: #ec1f27;
    --ink: #000000;
    --paper: #ffffff;
    --stage: #ececea;
    --muted: #9a9a9a;
    --soft: #cfcfcf;
  }
  * { margin: 0; padding: 0; box-sizing: border-box; }
  html, body { width: 1200px; height: 843px; overflow: hidden; }
  body {
    background: var(--stage);
    font-family: "Raleway", sans-serif;
    display: flex;
    align-items: center;
    justify-content: center;
    gap: 40px;
  }
  .card {
    position: relative;
    width: 540px;
    height: 308px;
    background: var(--ink);
    color: var(--paper);
    overflow: hidden;
    box-shadow: 0 6px 18px rgba(0,0,0,.25);
  }

  /* mascot artwork area */
  .mascot {
    position: absolute;
    border-radius: 6px;
    background: radial-gradient(ellipse at 50% 40%, #3a3a3a 0%, #161616 70%);
  }
  .brand-name {
    position: absolute;
    font-size: 14px;
    font-weight: 400;
    color: var(--paper);
    letter-spacing: .5px;
    white-space: nowrap;
    text-align: center;
  }

  /* front */
  .front .mascot { left: 40px; top: 48px; width: 176px; height: 196px; }
  .front .brand-name { left: 40px; width: 176px; top: 256px; }
  .company {
    position: absolute; left: 250px; top: 34px;
    font-variant: small-caps; font-size: 19px; font-weight: 400; letter-spacing: .5px;
    white-space: nowrap;
  }
  .person { position: absolute; left: 250px; top: 68px; }
  .person-name { font-size: 19px; font-weight: 300; color: var(--soft); text-transform: uppercase; letter-spacing: 1px; }
  .person-title { font-size: 9.5px; color: var(--muted); text-transform: uppercase; letter-spacing: 1px; margin-top: 1px; }
  .contacts { position: absolute; left: 250px; top: 124px; list-style: none; }
  .contact { display: flex; align-items: center; height: 24px; margin-bottom: 10px; }
  .contact-label {
    width: 92px; font-size: 9.5px; color: var(--muted);
    text-transform: uppercase; letter-spacing: .5px; white-space: nowrap;
  }
  .contact-value {
    display: flex; align-items: center;
    width: 184px; height: 24px; padding-left: 8px;
    background: var(--brand-red); color: var(--paper);
    font-size: 11px; font-weight: 300; white-space: nowrap;
  }
  .contact-value.large { font-size: 16px; }
  .address {
    position: absolute; left: 350px; top: 260px;
    font-size: 9px; color: var(--soft); text-transform: uppercase; letter-spacing: .8px; line-height: 1.3;
  }

  /* back */
  .rule { position: absolute; left: 0; width: 100%; height: 1px; background: var(--brand-red); }
  .rule.top { top: 38px; }
  .rule.bottom { top: 262px; }
  .back .mascot { left: 185px; top: 52px; width: 170px; height: 168px; }
  .back .brand-name { left: 185px; width: 170px; top: 230px; }
</style>
</head>
<body>
  <section class="card front">
    <div class="mascot" role="img" aria-label="Line-art mascot of a muscular technician in a hard hat holding a wrench"></div>
    <p class="brand-name">Brass Wheel Servicing</p>

    <h1 class="company">Brass Wheel Servicing</h1>
    <div class="person">
      <p class="person-name">Corwin Haldane</p>
      <p class="person-title">Service Technician</p>
    </div>
    <ul class="contacts">
      <li class="contact"><span class="contact-label">Website</span><span class="contact-value">www.brasswheelservicing.ca</span></li>
      <li class="contact"><span class="contact-label">Personal</span><span class="contact-value large">555-014-2280</span></li>
      <li class="contact"><span class="contact-label">Service Line</span><span class="contact-value large">555-014-7391</span></li>
      <li class="contact"><span class="contact-label">Service Email</span><span class="contact-value">service@brasswheel.ca</span></li>
    </ul>
    <p class="address">118 Larkfield Rd NW<br>Marlow AB T0X 2R4</p>
  </section>

  <section class="card back">
    <div class="rule top"></div>
    <div class="rule bottom"></div>
    <div class="mascot" role="img" aria-label="Line-art mascot of a muscular technician in a hard hat holding a wrench"></div>
    <p class="brand-name">Brass Wheel Servicing</p>
  </section>
</body>
</html>
```